Business and Success Coaching Business Card

Need a business card for my coaching business. I coach small businesses, career professionals and, individuals wanting to unlock their human potential and achieve excellence. At the heart of our methodology is the Shaping Purposeful Action Routines Knowingly (SPARK) approach to formulate empowerment, create principles for success and setting achievable outcomes. I would like something that incorporates our new logo, something clean and sharp with a solid darker, but complementary background, color on the card front. The back should be white where there will be room for three questions

Target Market(s)

People looking to advance and improve themselves through a success coach

Industry/Entity Type

Life Coaching

Contact Information for Business Card

Contact information on card.
Business name on front of card
Questions on back

Font styles to use
Other font styles liked:
• Century Gothic or other Serif style fonts that look similar to Century Gothic

Colors

Designer to choose colors to be used in the design.

Requirements
Must have
• Logo on front of card
• Business name - The Steady Forge
• Contact name - Ted Harlow
• Address - Box 4619, Littleton, CO 80127-4619
• Phone number - 303-555-0147
• Email address - harlow.ted@thesteadyforge.example
• Certifications - CSC, CCHt, PTT, PNLP
• Back of card
• Three questions on the back of the card:
• If you were at your best, what would you do right now?
• What is the decision you have been avoiding?
• What's one action you could take in the next 10 minutes?
Nice to have
• I would like to see a solid color on the front of the card that compliments the logo.
• Back should be white, or could be contrasting, but need to have the three questions.

```html
<!DOCTYPE html>
<html lang="en">
<head>
<meta charset="utf-8">
<title>The Steady Forge — Business Card</title>
<link rel="stylesheet" href="https://fonts.googleapis.com/css2?family=Jost:wght@400;500;600;700&family=Questrial&display=swap">
<style>
  :root {
    --navy: #22386f;
    --blue: #4684c6;
    --paper: #ffffff;
    --page: #eceef2;
    --edge: #c9cfdb;
  }
  * { box-sizing: border-box; margin: 0; padding: 0; }
  html, body { width: 1200px; height: 1199px; overflow: hidden; }
  body {
    background: var(--page);
    font-family: "Questrial", "Century Gothic", sans-serif;
    color: var(--navy);
    position: relative;
  }
  .card {
    position: absolute;
    left: 160px;
    width: 880px;
    height: 502px;
    background: var(--paper);
    border: 1px solid var(--edge);
    overflow: hidden;
    box-shadow: 0 6px 20px rgba(20, 30, 60, 0.12);
  }
  .card--front { top: 70px; }
  .card--back { top: 626px; }
  .card__art { position: absolute; inset: 0; width: 100%; height: 100%; }

  .brand {
    position: absolute;
    display: flex;
    align-items: center;
    gap: 10px;
    font-family: "Jost", sans-serif;
    font-weight: 600;
    color: var(--navy);
    white-space: nowrap;
  }
  .brand__dot { border-radius: 50%; background: var(--blue); flex: none; }
  .card--front .brand { top: 58px; right: 36px; font-size: 21px; }
  .card--front .brand__dot { width: 18px; height: 18px; }

  .person { position: absolute; left: 118px; top: 98px; display: inline-block; }
  .person__name {
    font-family: "Jost", sans-serif;
    font-weight: 600;
    font-size: 78px;
    line-height: 1;
    letter-spacing: -1px;
    text-transform: uppercase;
  }
  .person__certs {
    text-align: right;
    font-family: "Jost", sans-serif;
    font-size: 14px;
    margin-top: 4px;
    letter-spacing: 0.3px;
  }

  .details { position: absolute; left: 138px; top: 262px; font-size: 19px; line-height: 30px; }
  .details li { list-style: none; display: flex; align-items: center; gap: 9px; }
  .details svg { width: 17px; height: 17px; fill: var(--navy); flex: none; }

  .contact-tag {
    position: absolute;
    left: 84px; top: 446px;
    height: 36px;
    display: flex; align-items: center; gap: 8px;
    padding: 0 26px 0 4px;
    background: var(--navy);
    color: #cfe0f4;
    font-family: "Jost", sans-serif;
    font-weight: 600;
    font-size: 18px;
    letter-spacing: 2px;
    border-radius: 18px 0 0 18px;
    clip-path: polygon(0 0, 88% 0, 100% 50%, 88% 100%, 0 100%);
  }
  .contact-tag__icon {
    width: 30px; height: 30px; border-radius: 50%;
    border: 2px solid #cfe0f4;
    display: flex; align-items: center; justify-content: center;
  }
  .contact-tag__icon svg { width: 16px; height: 16px; fill: #cfe0f4; }
  .phone { position: absolute; left: 258px; top: 436px; font-size: 40px; color: var(--navy); letter-spacing: 0.5px; }

  .card--back .brand { top: 150px; left: 0; right: 0; justify-content: center; font-size: 34px; }
  .card--back .brand__dot { width: 28px; height: 28px; }
  .questions { position: absolute; left: 70px; top: 268px; font-family: "Jost", sans-serif; font-weight: 500; font-size: 25px; line-height: 37px; }
  .questions li { list-style: none; padding-left: 26px; position: relative; }
  .questions li::before {
    content: ""; position: absolute; left: 3px; top: 15px;
    width: 8px; height: 8px; border-radius: 50%; background: var(--navy);
  }
</style>
</head>
<body>

<section class="card card--front" aria-label="Card front">
  <svg class="card__art" viewBox="0 0 545 311" preserveAspectRatio="none" aria-hidden="true">
    <polygon points="0,240 378,240 545,80 545,311 0,311" fill="#22386f"/>
    <polygon points="0,258 384,258 545,104 545,118 352,311 0,311" fill="#4684c6"/>
    <line x1="396" y1="311" x2="545" y2="168" stroke="#4684c6" stroke-width="7"/>
    <line x1="442" y1="311" x2="545" y2="212" stroke="#4684c6" stroke-width="7"/>
    <line x1="488" y1="311" x2="545" y2="256" stroke="#4684c6" stroke-width="7"/>
  </svg>

  <div class="brand"><span class="brand__dot"></span>The Steady Forge</div>

  <div class="person">
    <h1 class="person__name">Ted Harlow</h1>
    <p class="person__certs">CSC, CCHt, PTT, PNLP</p>
  </div>

  <ul class="details">
    <li><svg viewBox="0 0 16 16"><path d="M8 1 0 8h2v7h4v-5h4v5h4V8h2z"/></svg>Box 4619, Littleton, CO 80127-4619</li>
    <li><svg viewBox="0 0 16 16"><path d="M0 3h16v10H0zM1 4l7 5 7-5v-.2H1z" fill-rule="evenodd"/></svg>harlow.ted@thesteadyforge.example</li>
  </ul>

  <div class="contact-tag">
    <span class="contact-tag__icon"><svg viewBox="0 0 16 16"><path d="M3 2h3l1 3-2 1a8 8 0 0 0 5 5l1-2 3 1v3c0 1-1 1-1 1C7 14 2 9 2 3c0 0 0-1 1-1z"/></svg></span>
    CONTACT
  </div>
  <p class="phone">303-555-0147</p>
</section>

<section class="card card--back" aria-label="Card back">
  <svg class="card__art" viewBox="0 0 545 311" preserveAspectRatio="none" aria-hidden="true">
    <polygon points="0,0 92,0 0,90" fill="#22386f"/>
    <polygon points="545,220 545,311 452,311" fill="#22386f"/>
  </svg>

  <div class="brand"><span class="brand__dot"></span>The Steady Forge</div>

  <ul class="questions">
    <li>If you were at your best, what would you do right now?</li>
    <li>What is the decision you have been avoiding?</li>
    <li>What's one action you could take in the next 10 minutes?</li>
  </ul>
</section>

</body>
</html>
```